Quellan and Dermal Fillers

We need a poster designed to display outside our dental practice to advertise that we offer quellan and dermal fillers

Industry/Entity Type

Dental

```html
<!DOCTYPE html>
<html lang="en">
<head>
<meta charset="utf-8">
<title>Quellan &amp; Dermal Fillers Poster</title>
<link rel="stylesheet" href="https://fonts.googleapis.com/css2?family=Raleway:wght@300&family=Great+Vibes&display=swap">
<style>
  :root {
    --paper: #f5f5f4;
    --paper-light: #fbfbfb;
    --ink: #8c8c8c;
    --frame: #9a9a9a;
    --accent: #d9899a;
    --skin-light: #f1d9cb;
    --skin: #e2bba6;
    --skin-shade: #c99a82;
    --hair: #9a7358;
  }
  html, body {
    margin: 0;
    padding: 0;
    overflow: hidden;
  }
  .poster {
    position: relative;
    width: 849px;
    height: 1200px;
    overflow: hidden;
    background: radial-gradient(ellipse at 20% 20%, var(--paper-light), var(--paper) 70%);
    font-family: "Raleway", sans-serif;
  }
  .portrait-photo {
    position: absolute;
    left: 330px;
    top: 0;
    width: 519px;
    height: 1200px;
    background:
      radial-gradient(ellipse 55% 12% at 75% 4%, var(--hair), transparent 100%),
      radial-gradient(ellipse 62% 44% at 72% 42%, var(--skin-light) 0%, var(--skin) 60%, var(--skin-shade) 85%, transparent 100%),
      radial-gradient(ellipse 40% 30% at 70% 92%, var(--skin) 0%, transparent 100%);
  }
  .frames {
    position: absolute;
    inset: 0;
  }
  .headline {
    position: absolute;
    left: 142px;
    top: 540px;
    margin: 0;
    font-weight: 300;
    font-size: 50px;
    line-height: 57px;
    letter-spacing: 1px;
    color: var(--ink);
    text-transform: uppercase;
  }
  .headline span {
    display: block;
  }
  .ampersand {
    position: absolute;
    left: 334px;
    top: 702px;
    font-family: "Great Vibes", cursive;
    font-size: 64px;
    line-height: 1;
    color: var(--accent);
  }
</style>
</head>
<body>
<main class="poster">
  <div class="portrait-photo" role="img" aria-label="Close-up portrait photograph of a woman's face, split into panels comparing younger and older skin"></div>

  <svg class="frames" width="849" height="1200" viewBox="0 0 849 1200" aria-hidden="true">
    <g fill="none" stroke="var(--frame)" stroke-width="3">
      <rect x="444" y="93" width="297" height="232"/>
      <rect x="741" y="325" width="130" height="212"/>
      <rect x="425" y="538" width="297" height="263"/>
      <rect x="708" y="849" width="160" height="240"/>
    </g>
  </svg>

  <h1 class="headline">
    <span>We</span>
    <span>Offer</span>
    <span>Quellan</span>
    <span>Derma</span>
    <span>Fillers</span>
  </h1>
  <div class="ampersand" aria-hidden="true">&amp;</div>
</main>
</body>
</html>
```